New Business Card Design*

We are a recruitment company based in Norwich/Cambridge England.
I have included our company logo which we want to remain the same.

What we are looking for is a new creative Business card which will really stand out!!

Contact Information for Business Card

Harriet Vance
email: Harriet@brelvix.co.uk
Address: Tolworth House
Ashgrove Innovation Park
Pelham Road
Norwich
KT9 3QD
Tel:01632 960418

```html
<!DOCTYPE html>
<html lang="en">
<head>
<meta charset="utf-8">
<title>Harriet Vance – Brelvix Business Card</title>
<link rel="stylesheet" href="https://fonts.googleapis.com/css2?family=Montserrat:wght@400;500;600&display=swap">
<style>
  :root {
    --card-white: #ffffff;
    --brand-green: #8dc63f;
    --band-green: #678b33;
    --fold-green: #4f6d25;
    --icon-grey: #8e8a8e;
    --icon-green: #678b33;
    --ink: #1f1f1f;
    --logo-grey: #8a868a;
    --strip-grey: #f1f1f1;
    --mesh-tint: #e4e4e4;
  }
  * { margin: 0; padding: 0; box-sizing: border-box; }
  html, body {
    width: 1200px;
    height: 686px;
    overflow: hidden;
    background: var(--card-white);
  }
  .card {
    position: relative;
    width: 1200px;
    height: 686px;
    overflow: hidden;
    background: var(--card-white);
    font-family: "Montserrat", sans-serif;
  }
  .mesh-decor {
    position: absolute;
    left: 0;
    width: 640px;
  }
  .mesh-decor--top { top: 0; height: 250px; }
  .mesh-decor--bottom { bottom: 0; height: 130px; }

  .divider-strip {
    position: absolute;
    left: 640px;
    top: 0;
    width: 37px;
    height: 686px;
    background: var(--strip-grey);
  }
  .contact-panel {
    position: absolute;
    left: 677px;
    top: 0;
    width: 523px;
    height: 686px;
    background: var(--brand-green);
  }

  .icon-box {
    position: absolute;
    width: 57px;
    height: 57px;
    display: flex;
    align-items: center;
    justify-content: center;
  }
  .icon-box--grey { background: var(--icon-grey); }
  .icon-box--green { background: var(--icon-green); }

  .phone-icon { left: 69px; top: 143px; }
  .phone-number {
    position: absolute;
    left: 139px;
    top: 155px;
    font-size: 25px;
    font-weight: 400;
    letter-spacing: 1px;
    color: var(--ink);
  }

  .email-icon { left: 754px; top: 143px; }
  .email-address {
    position: absolute;
    left: 841px;
    top: 152px;
    font-size: 25px;
    font-weight: 400;
    letter-spacing: 0.6px;
    color: var(--card-white);
  }

  .pin-icon { left: 754px; top: 251px; }
  .postal-address {
    position: absolute;
    left: 841px;
    top: 248px;
    font-size: 25px;
    font-weight: 400;
    line-height: 28.6px;
    letter-spacing: 0.6px;
    color: var(--card-white);
    font-style: normal;
  }

  .name-band {
    position: absolute;
    left: 639px;
    top: 455px;
    width: 561px;
    height: 86px;
    background: var(--band-green);
    display: flex;
    align-items: center;
    justify-content: center;
    padding-left: 20px;
  }
  .holder-name {
    font-size: 50px;
    font-weight: 500;
    letter-spacing: 1px;
    color: var(--card-white);
    text-transform: uppercase;
  }
  .band-fold {
    position: absolute;
    left: 639px;
    width: 38px;
  }
  .band-fold--top { top: 437px; height: 18px; }
  .band-fold--bottom { top: 541px; height: 21px; }

  .brand-mark {
    position: absolute;
    left: 69px;
    top: 460px;
    width: 80px;
    height: 80px;
    border-radius: 50%;
    background: var(--brand-green);
  }
  .brand-name {
    position: absolute;
    left: 166px;
    top: 466px;
    font-size: 54px;
    font-weight: 600;
    color: var(--logo-grey);
    letter-spacing: 0.5px;
  }
</style>
</head>
<body>
<main class="card">
  <svg class="mesh-decor mesh-decor--top" role="img" aria-label="Faint network-style mesh of connected grey dots and lines" viewBox="0 0 640 250" preserveAspectRatio="none">
    <defs>
      <radialGradient id="meshGlowTop" cx="45%" cy="0%" r="80%">
        <stop offset="0" stop-color="var(--mesh-tint)" stop-opacity="0.55"/>
        <stop offset="1" stop-color="var(--mesh-tint)" stop-opacity="0"/>
      </radialGradient>
    </defs>
    <rect width="640" height="250" fill="url(#meshGlowTop)"/>
  </svg>
  <svg class="mesh-decor mesh-decor--bottom" role="img" aria-label="Faint network-style mesh of connected grey dots and lines" viewBox="0 0 640 130" preserveAspectRatio="none">
    <defs>
      <linearGradient id="meshGlowBottom" x1="0" y1="1" x2="0" y2="0">
        <stop offset="0" stop-color="var(--mesh-tint)" stop-opacity="0.5"/>
        <stop offset="1" stop-color="var(--mesh-tint)" stop-opacity="0"/>
      </linearGradient>
    </defs>
    <rect width="640" height="130" fill="url(#meshGlowBottom)"/>
  </svg>

  <div class="divider-strip"></div>
  <div class="contact-panel"></div>

  <div class="icon-box icon-box--grey phone-icon">
    <svg width="26" height="26" viewBox="0 0 24 24" aria-hidden="true">
      <path fill="#ffffff" d="M6.6 10.8a15.1 15.1 0 0 0 6.6 6.6l2.2-2.2c.3-.3.7-.4 1-.2 1.1.4 2.3.6 3.6.6.6 0 1 .4 1 1V20c0 .6-.4 1-1 1A17 17 0 0 1 3 4c0-.6.4-1 1-1h3.5c.6 0 1 .4 1 1 0 1.3.2 2.5.6 3.6.1.3 0 .7-.2 1z"/>
    </svg>
  </div>
  <p class="phone-number">01632960418</p>

  <div class="icon-box icon-box--green email-icon">
    <svg width="28" height="20" viewBox="0 0 28 20" aria-hidden="true">
      <rect x="1" y="1" width="26" height="18" fill="none" stroke="#ffffff" stroke-width="2"/>
      <path d="M1 1 L14 11 L27 1" fill="none" stroke="#ffffff" stroke-width="2"/>
    </svg>
  </div>
  <p class="email-address">Harriet@brelvix.co.uk</p>

  <div class="icon-box icon-box--green pin-icon">
    <svg width="20" height="28" viewBox="0 0 20 28" aria-hidden="true">
      <path fill="#ffffff" d="M10 0a10 10 0 0 0-10 10c0 7.5 10 18 10 18s10-10.5 10-18A10 10 0 0 0 10 0zm0 14a4 4 0 1 1 0-8 4 4 0 0 1 0 8z"/>
    </svg>
  </div>
  <address class="postal-address">
    Tolworth House<br>
    Ashgrove Innovation Park<br>
    Pelham Road<br>
    Norwich<br>
    KT9 3QD
  </address>

  <svg class="band-fold band-fold--top" viewBox="0 0 38 18" preserveAspectRatio="none" aria-hidden="true">
    <polygon points="38,0 38,18 0,18" fill="var(--fold-green)"/>
  </svg>
  <div class="name-band">
    <h1 class="holder-name">Harriet Vance</h1>
  </div>
  <svg class="band-fold band-fold--bottom" viewBox="0 0 38 21" preserveAspectRatio="none" aria-hidden="true">
    <polygon points="0,0 38,0 38,21" fill="var(--fold-green)"/>
  </svg>

  <div class="brand-mark" aria-hidden="true"></div>
  <p class="brand-name">Brelvix</p>
</main>
</body>
</html>
```